Rock, Paper Scissors Championship Flyer

We need a dynamic, bold and exciting flyer to promote the following event at our sports center. The event will be primarily focused for adults, but children are welcome to join

Rock, Paper, Scissors Championship - $$$ prizes
Date: June 9th, 2018
Time: 11am-4pm
Fee: $2 to enter, free for spectators
Heats to determine the overall ‘Rock, Paper, Scissors’ champion!
- Cash prizes on offer
- Live music.
- Food and beverage available for purchase

Belmoray Sports Center, Harrowvale NJ
908-555-0163
www.belmoraypark.example

Must include our logo (does not have to be huge) and County seal (both attached)

Colors

Designer to choose colors to be used in the design.

Requirements
Must have
• Should be fun and colorful
• The following info and attached logos:
• Rock, Paper, Scissors Championship - $$$ prizes
• Date: June 9th, 2018
• Time: 11am-4pm
• Fee: $2 to enter, free for spectators
• Heats to determine the overall ‘Rock, Paper, Scissors’ champion!
• - Cash prizes on offer
• - Live music.
• - Food and beverage available for purchase
• Belmoray Sports Center, Harrowvale NJ
• 908-555-0163
• www.belmoraypark.example
Nice to have
• There are a few inspirational photos attached to give an idea of what we are looking for.

```html
<!DOCTYPE html>
<html lang="en">
<head>
<meta charset="utf-8">
<title>Rock Paper Scissors Championship Flyer</title>
<link rel="stylesheet" href="https://fonts.googleapis.com/css2?family=Anton&family=Oswald:wght@500;700&family=Montserrat:wght@500;600&display=swap">
<style>
  :root {
    --stage: #a9a9a9;
    --navy: #0f3764;
    --band: #173c69;
    --rock-light: #8d8a7c;
    --rock-mid: #6b665a;
    --rock-dark: #3a342d;
    --forest-teal: #2f6f78;
    --forest-deep: #10304f;
    --seal-gold: #c9a35a;
    --white: #ffffff;
  }
  * { margin: 0; padding: 0; box-sizing: border-box; }
  html, body { width: 1200px; height: 2190px; overflow: hidden; }
  body { background: var(--stage); position: relative; }

  .flyer {
    position: absolute; left: 50px; top: 317px;
    width: 1100px; height: 1556px;
    background: var(--navy);
    overflow: hidden;
    color: var(--white);
    box-shadow: 0 6px 18px rgba(0,0,0,.35);
  }
  .flyer > * { position: absolute; }

  .rock-texture {
    left: 0; top: 120px; width: 1100px; height: 1236px;
    background: linear-gradient(180deg, var(--rock-light) 0%, var(--rock-mid) 45%, var(--rock-light) 75%, var(--rock-mid) 100%);
  }
  .rock-shadow-left {
    left: 0; top: 258px; width: 380px; height: 400px;
    background: linear-gradient(180deg, var(--rock-dark), rgba(58,52,45,.45));
  }
  .rock-shadow-right {
    left: 860px; top: 236px; width: 240px; height: 630px;
    background: linear-gradient(180deg, var(--rock-dark), rgba(58,52,45,.5));
  }
  .forest {
    left: 0; top: 1229px; width: 1100px; height: 327px;
    background: linear-gradient(180deg, rgba(47,111,120,.85) 0%, var(--forest-teal) 25%, var(--forest-deep) 70%, var(--navy) 100%);
  }

  .brand {
    left: 42px; top: 34px; width: 180px;
    display: flex; flex-direction: column; align-items: center; gap: 10px;
    font-family: "Oswald", sans-serif; font-weight: 500; font-size: 24px;
    line-height: 1.1; text-align: center; text-transform: uppercase; letter-spacing: 1px;
  }
  .brand-dot { width: 60px; height: 60px; border-radius: 50%; background: var(--white); }

  .county-seal {
    left: 900px; top: 42px; width: 143px; height: 143px; border-radius: 50%;
    background: var(--seal-gold);
  }

  .headline {
    left: 0; top: 186px; width: 1100px; text-align: center;
    font-family: "Anton", sans-serif; font-weight: 400;
    font-size: 104px; line-height: 112px; text-transform: uppercase; letter-spacing: 2px;
  }

  .hands {
    left: 400px; top: 520px; width: 380px; height: 330px;
    background: radial-gradient(ellipse at center, rgba(29,59,102,.75) 0%, rgba(29,59,102,.35) 60%, rgba(29,59,102,0) 100%);
  }

  .event-date {
    left: 53px; top: 515px;
    font-family: "Oswald", sans-serif; font-weight: 700;
    font-size: 62px; line-height: 68px;
  }
  .event-time {
    left: 53px; top: 715px;
    font-family: "Oswald", sans-serif; font-weight: 500;
    font-size: 34px; line-height: 40px;
  }

  .fees {
    right: 64px; top: 515px; text-align: right;
    font-family: "Oswald", sans-serif; font-weight: 700;
  }
  .fee-label { font-size: 56px; line-height: 62px; }
  .fee-amount { font-size: 116px; line-height: 116px; }
  .fee-free { font-size: 46px; line-height: 50px; margin-top: 8px; }
  .fee-spectators { font-size: 30px; line-height: 34px; }

  .championship {
    left: 0; top: 846px; width: 1100px; text-align: center;
    font-family: "Anton", sans-serif; font-weight: 400;
    font-size: 100px; line-height: 110px; text-transform: uppercase; letter-spacing: 2px;
  }

  .prize-band {
    left: 0; top: 966px; width: 1035px; height: 108px;
    background: var(--band);
    display: flex; align-items: center; justify-content: center;
    padding-left: 65px;
    font-family: "Montserrat", sans-serif; font-weight: 600; font-size: 62px;
  }

  .highlights {
    left: 0; top: 1098px; width: 1100px; list-style: none; text-align: center;
    font-family: "Montserrat", sans-serif; font-weight: 600;
    font-size: 39px; line-height: 49px;
    text-shadow: 0 1px 3px rgba(0,0,0,.35);
  }

  .contact {
    left: 0; top: 1352px; width: 1100px; list-style: none;
    display: flex; flex-direction: column; align-items: center;
    font-family: "Montserrat", sans-serif; font-weight: 600; font-size: 24px;
  }
  .contact li { display: flex; flex-direction: column; align-items: center; gap: 4px; margin-bottom: 10px; }
  .contact svg { width: 20px; height: 20px; }
</style>
</head>
<body>
  <main class="flyer">
    <div class="rock-texture" role="img" aria-label="Weathered grey rock cliff texture"></div>
    <div class="rock-shadow-left"></div>
    <div class="rock-shadow-right"></div>
    <div class="forest" role="img" aria-label="Teal pine forest silhouette fading into navy"></div>

    <div class="brand">
      <span class="brand-dot"></span>
      <span>Belmoray Sports Center</span>
    </div>
    <div class="county-seal" role="img" aria-label="County seal"></div>

    <h1 class="headline">Rock<br>Paper<br>Scissors</h1>

    <div class="hands" role="img" aria-label="Navy hand signs for rock, paper and scissors"></div>

    <p class="event-date">June 9th,<br>2018</p>
    <p class="event-time">Time:<br>11am-4pm</p>

    <div class="fees">
      <p class="fee-label">Entry Fee:</p>
      <p class="fee-amount">$2</p>
      <p class="fee-free">FREE for</p>
      <p class="fee-spectators">SPECTATORS</p>
    </div>

    <h2 class="championship">Championship</h2>
    <div class="prize-band">$$$ prizes</div>

    <ul class="highlights">
      <li>Cash prizes on offer</li>
      <li>Live music.</li>
      <li>Food and beverage available for purchase</li>
    </ul>

    <ul class="contact">
      <li>
        <svg viewBox="0 0 20 20" aria-hidden="true"><path d="M10 2a6 6 0 0 0-6 6c0 4.5 6 10 6 10s6-5.5 6-10a6 6 0 0 0-6-6zm0 8.2A2.2 2.2 0 1 1 10 5.8a2.2 2.2 0 0 1 0 4.4z" fill="none" stroke="#fff" stroke-width="1.5"/></svg>
        <span>Belmoray Sports Center, Harrowvale NJ</span>
      </li>
      <li>
        <svg viewBox="0 0 20 20" aria-hidden="true"><path d="M5 2.5l3 .5 1 3.5-2 1.5a9 9 0 0 0 5 5l1.5-2 3.5 1 .5 3-2 2C9 17 3 11 3 4.5z" fill="#fff"/></svg>
        <span>908-555-0163</span>
      </li>
      <li>
        <svg viewBox="0 0 20 20" aria-hidden="true"><g fill="none" stroke="#fff" stroke-width="1.4"><circle cx="10" cy="10" r="8"/><ellipse cx="10" cy="10" rx="3.5" ry="8"/><path d="M2 10h16M3.5 6h13M3.5 14h13"/></g></svg>
        <span>www.belmoraypark.example</span>
      </li>
    </ul>
  </main>
</body>
</html>
```